varnok llc

excavating and landscaping

Target Market(s)

Industry/Entity Type

Contact Information for Business Card

file atach

Font styles to use
Serif

```html
<!DOCTYPE html>
<html lang="en">
<head>
<meta charset="utf-8">
<title>Varnok LLC — Business Card</title>
<link href="https://fonts.googleapis.com/css2?family=Montserrat:wght@700;800&family=Roboto:wght@300;400&display=swap" rel="stylesheet">
<style>
  :root{
    --bg:#3b3b3d;
    --red:#d91f26;
    --red-dark:#b5161c;
    --ink:#151515;
    --grey:#4a4a4a;
    --rule:#9a9a9a;
    --white:#ffffff;
    --card-w:540px;
    --card-h:309px;
  }
  *{box-sizing:border-box;margin:0;padding:0}
  html,body{width:1200px;height:801px;overflow:hidden;background:var(--bg)}
  .stage{position:relative;width:1200px;height:801px;display:flex;align-items:center;justify-content:center;gap:40px}
  .card{position:relative;width:var(--card-w);height:var(--card-h);border-radius:14px;overflow:hidden;box-shadow:0 10px 24px rgba(0,0,0,.35)}

  /* back */
  .card--back{border-bottom:3px solid var(--red)}
  .card__photo{position:absolute;inset:0;background:linear-gradient(160deg,#2a2a2c 0%,#1d1b1a 45%,#2e2520 75%,#1a1816 100%)}
  .brand{position:absolute;font-family:"Montserrat",sans-serif;font-weight:800;letter-spacing:1px;text-transform:uppercase;white-space:nowrap}
  .card--back .brand{left:50%;top:50%;transform:translate(-50%,-50%);font-size:56px;color:var(--white);display:flex;align-items:center;gap:14px}
  .brand__dot{width:16px;height:16px;background:var(--red);border-radius:50%;display:inline-block}

  /* front */
  .card--front{background:var(--white)}
  .card--front .brand{left:34px;top:128px;width:262px;font-size:30px;color:var(--ink);display:flex;align-items:center;gap:9px}
  .card--front .brand__dot{width:11px;height:11px}
  .divider{position:absolute;left:318px;top:34px;width:1px;height:168px;background:var(--rule)}
  .divider__accent{position:absolute;left:-1px;top:56px;width:3px;height:58px;background:var(--red)}
  .contact{position:absolute;left:336px;top:30px;font-family:"Roboto",sans-serif;color:var(--grey)}
  .contact__name{font-family:"Montserrat",sans-serif;font-weight:800;font-size:22px;color:var(--red);letter-spacing:.3px}
  .contact__role{font-size:14px;font-weight:300;margin-top:4px}
  .contact__rule{width:34px;height:2px;background:var(--red);margin:5px 0 6px}
  .contact__line{font-size:13.5px;font-weight:400;line-height:19px;display:flex;align-items:center;gap:7px}
  .contact__line svg{width:12px;height:12px;flex:none}
  .band{position:absolute;left:0;right:0;top:238px;height:40px;background:linear-gradient(90deg,var(--red-dark),var(--red));display:flex;align-items:center;justify-content:center}
  .band__text{font-family:"Montserrat",sans-serif;font-weight:700;font-size:16px;color:var(--white);letter-spacing:1.2px;text-transform:uppercase}
</style>
</head>
<body>
<main class="stage">
  <section class="card card--back">
    <div class="card__photo" role="img" aria-label="Dimmed photo of backhoes on a dirt site in front of a building"></div>
    <div class="brand"><span class="brand__dot"></span>Varnok LLC</div>
  </section>

  <section class="card card--front">
    <div class="brand"><span class="brand__dot"></span>Varnok LLC</div>
    <div class="divider"><span class="divider__accent"></span></div>
    <div class="contact">
      <div class="contact__name">DALE RENNER</div>
      <div class="contact__role">Founder</div>
      <div class="contact__rule"></div>
      <div class="contact__line">48 Alder Street</div>
      <div class="contact__line">Millbrook, MA 01790</div>
      <div class="contact__rule"></div>
      <div class="contact__line">
        <svg viewBox="0 0 24 24"><path fill="#d91f26" d="M6.6 10.8a15 15 0 0 0 6.6 6.6l2.2-2.2a1 1 0 0 1 1-.25 11.4 11.4 0 0 0 3.6.57 1 1 0 0 1 1 1V20a1 1 0 0 1-1 1A17 17 0 0 1 3 4a1 1 0 0 1 1-1h3.5a1 1 0 0 1 1 1c0 1.250.2 2.450.57 3.570a1 1 0 0 1-.25 1z"/></svg>
        555-014-2290
      </div>
      <div class="contact__line">
        <svg viewBox="0 0 24 24"><rect x="2" y="5" width="20" height="14" rx="1" fill="#d91f26"/><path d="M3 6l9 7 9-7" fill="none" stroke="#fff" stroke-width="1.6"/></svg>
        office@varnokllc.com
      </div>
      <div class="contact__line">
        <svg viewBox="0 0 24 24"><circle cx="12" cy="12" r="10" fill="#d91f26"/><path d="M2 12h20M12 2c3 3 3 17 0 20M12 2c-3 3-3 17 0 20" fill="none" stroke="#fff" stroke-width="1.4"/></svg>
        varnokllc.com
      </div>
    </div>
    <div class="band"><span class="band__text">Excavating and Landscaping</span></div>
  </section>
</main>
</body>
</html>
```